Wedding Thank You post card

We would like to design a thank you post card for our wedding guests.
We want it to be a classic style with our photo and a simple 'Thank you' written and then Tom and Sylvia 15.03.2014' Where the writing does not obstruct our image.
We need 140 post cards
Sorry for the delay please find some photos you can use for the design process. One or all photos can be used. Thank you
Wedding

```html
<!DOCTYPE html>
<html lang="en">
<head>
<meta charset="utf-8">
<title>Wedding Thank You Postcard</title>
<link rel="stylesheet" href="https://fonts.googleapis.com/css2?family=Pinyon+Script&display=swap">
<style>
  :root {
    --panel-green: #cde07e;
    --ink: #161616;
    --accent-red: #b3261e;
    --photo-light: #d9d9d9;
    --photo-mid: #8a8a8a;
    --photo-dark: #3a3a3a;
    --flourish-dark: #5f6b3a;
  }
  html, body {
    margin: 0;
    padding: 0;
    width: 1200px;
    height: 930px;
    overflow: hidden;
    background: #ffffff;
  }
  .postcard {
    position: relative;
    width: 1200px;
    height: 930px;
    overflow: hidden;
    background: var(--panel-green);
  }
  .couple-photo {
    position: absolute;
    left: 0;
    top: 0;
    width: 607px;
    height: 930px;
    background:
      radial-gradient(ellipse 120px 260px at 420px 540px, rgba(255,255,255,0.75), rgba(255,255,255,0) 100%),
      linear-gradient(180deg, var(--photo-light) 0%, var(--photo-mid) 45%, var(--photo-dark) 75%, var(--photo-mid) 100%);
  }
  .message-panel {
    position: absolute;
    left: 607px;
    top: 0;
    width: 593px;
    height: 930px;
    font-family: "Pinyon Script", cursive;
    color: var(--ink);
  }
  .headline {
    position: absolute;
    left: 38px;
    top: 40px;
    margin: 0;
    font-weight: 400;
    font-size: 104px;
    line-height: 1;
    white-space: nowrap;
    letter-spacing: 1px;
  }
  .headline-tag {
    position: absolute;
    left: 418px;
    top: 172px;
    font-size: 22px;
    color: var(--accent-red);
    white-space: nowrap;
  }
  .wedding-date {
    position: absolute;
    left: 71px;
    top: 288px;
    margin: 0;
    font-size: 32px;
    white-space: nowrap;
  }
  .wedding-date sup {
    font-size: 18px;
    vertical-align: 12px;
  }
  .flourish {
    position: absolute;
    left: 40px;
    top: 350px;
    width: 553px;
    height: 490px;
    background: radial-gradient(ellipse 52% 48% at 60% 50%, rgba(95,107,58,0.45) 0%, rgba(95,107,58,0.15) 60%, rgba(95,107,58,0) 100%);
  }
  .sign-off {
    position: absolute;
    left: 38px;
    top: 785px;
    margin: 0;
    font-size: 40px;
    line-height: 60px;
    white-space: nowrap;
  }
</style>
</head>
<body>
  <main class="postcard">
    <div class="couple-photo" role="img" aria-label="Black and white photo of the bride and groom on the steps of a stone house doorway beside a lion statue and a white lantern"></div>
    <section class="message-panel">
      <h1 class="headline">Thanks You</h1>
      <span class="headline-tag">So Much</span>
      <p class="wedding-date">15<sup>th</sup> March 2014</p>
      <div class="flourish" role="img" aria-label="Decorative swirling olive green flourish ornament"></div>
      <p class="sign-off">With Love,<br>Tom and Sylvia</p>
    </section>
  </main>
</body>
</html>
```